Swimming pool service business postcard redesign

We need a fresh post card design for our pool service business based in San Diego called Tide Sweepers. We are a family based, local residential pool cleaning and maintenance company. we need an offer to stand out, our logo, our colors, etc on a 5.5x8 inch full color post card.

```html
<!DOCTYPE html>
<html lang="en">
<head>
<meta charset="utf-8">
<title>Tide Sweepers Postcard</title>
<link href="https://fonts.googleapis.com/css2?family=Archivo+Black&family=Bebas+Neue&family=Kaushan+Script&family=Montserrat:wght@500;600;700;800&family=Oswald:ital,wght@0,500;0,600;1,500&display=swap" rel="stylesheet">
<style>
:root{
  --navy:#1d4f91;
  --deep:#163f78;
  --orange:#e8672a;
  --red:#e0412b;
  --cream:#ece8dc;
  --ink:#222222;
  --white:#ffffff;
  --line:#9a9a9a;
  --pool-a:#1e8fc4;
  --pool-b:#39b4dc;
  --pool-c:#1670a8;
}
*{box-sizing:border-box;margin:0;padding:0}
html,body{width:1200px;height:825px;overflow:hidden;background:var(--white)}
.canvas{position:relative;width:1200px;height:825px;overflow:hidden;font-family:"Montserrat",sans-serif}
.abs{position:absolute}

/* front */
.front{left:8px;top:8px;width:1184px;height:420px;overflow:hidden}
.pool-photo{inset:0;background:linear-gradient(120deg,var(--pool-b) 0%,var(--pool-a) 45%,var(--pool-c) 100%)}
.brand-mark{left:56px;top:22px;width:360px;height:345px;border-radius:50%;background:var(--red);border:10px solid var(--white)}
.brand-name{left:56px;top:150px;width:360px;text-align:center;font-family:"Archivo Black",sans-serif;font-size:54px;line-height:1;color:var(--white)}
.headline{left:458px;top:20px;font-family:"Bebas Neue",sans-serif;font-size:92px;line-height:1;color:var(--cream);letter-spacing:1px;transform:rotate(-4deg);transform-origin:left bottom}
.script{left:470px;top:82px;font-family:"Kaushan Script",cursive;font-size:58px;color:var(--cream);transform:rotate(-7deg);transform-origin:left bottom;white-space:nowrap}
.tagline{left:530px;top:150px;font-family:"Montserrat",sans-serif;font-weight:700;font-size:18px;line-height:1.25;letter-spacing:2px;color:var(--cream);text-align:center;transform:rotate(-5deg)}
.city-badge{left:970px;top:65px;width:128px;height:128px;border-radius:50%;background:linear-gradient(180deg,#3b4f8a,var(--orange));border:5px solid var(--cream)}
.offer{left:526px;top:200px;width:482px;height:156px;background:var(--cream);border:2px dashed #555;border-radius:18px;transform:rotate(-1.5deg)}
.offer-get{left:22px;top:34px;font-family:"Archivo Black",sans-serif;font-size:42px;line-height:1;color:var(--ink)}
.offer-amount{left:116px;top:4px;font-family:"Archivo Black",sans-serif;font-size:100px;line-height:1;color:var(--orange);letter-spacing:-5px;white-space:nowrap}
.offer-amount sup{font-size:50px;vertical-align:36px;letter-spacing:0}
.offer-copy{left:290px;top:18px;font-family:"Archivo Black",sans-serif;font-size:23px;line-height:1.18;color:var(--ink)}
.offer-pill{left:32px;top:114px;width:416px;height:30px;border-radius:8px;background:var(--ink);display:flex;align-items:center;justify-content:center;gap:12px;color:var(--white);font-family:"Oswald",sans-serif;font-style:italic;font-weight:500;font-size:19px;letter-spacing:1px}
.trust-bar{left:0;top:372px;width:1184px;height:48px;background:linear-gradient(90deg,var(--red),#8a6080 45%,var(--navy) 80%)}
.trust-item{top:0;height:48px;display:flex;align-items:center;gap:14px;font-family:"Oswald",sans-serif;font-weight:500;font-size:17px;color:var(--white);letter-spacing:.3px;white-space:nowrap}
.trust-family{left:36px}
.trust-guarantee{left:280px}
.trust-licensed{left:562px}
.contact-tab{left:842px;top:344px;width:342px;height:76px;background:var(--orange);clip-path:polygon(14% 0,100% 0,100% 100%,0 100%)}
.phone-disc{left:900px;top:360px;width:46px;height:46px;border-radius:50%;background:var(--white);display:flex;align-items:center;justify-content:center}
.tab-phone{left:960px;top:352px;font-family:"Montserrat",sans-serif;font-weight:800;font-size:32px;color:var(--white);letter-spacing:.5px}
.tab-site{left:992px;top:388px;font-family:"Oswald",sans-serif;font-weight:500;font-size:22px;color:var(--white)}

/* back */
.back{left:8px;top:435px;width:1184px;height:378px;border:1px solid var(--line);background:var(--white)}
.services-title{left:34px;top:20px;font-family:"Montserrat",sans-serif;font-weight:800;font-size:25px;color:var(--navy);transform:rotate(-2deg)}
.services-script{left:48px;top:40px;font-family:"Kaushan Script",cursive;font-size:44px;color:var(--orange);transform:rotate(-4deg)}
.services-rule{left:56px;top:95px;width:160px;height:4px;background:var(--orange);border-radius:2px;transform:rotate(-4deg)}
.truck-photo{left:50px;top:112px;width:176px;height:56px;border-radius:10px;background:linear-gradient(90deg,var(--red),var(--navy) 55%,var(--pool-b))}
.service-list{left:36px;top:172px;list-style:none}
.service-list li{display:flex;align-items:center;gap:8px;height:21px;font-weight:700;font-size:12.6px;color:var(--navy)}
.photo-pool{left:292px;top:12px;width:252px;height:171px;background:linear-gradient(135deg,#6e9a3a,#2fb3e6 50%,#8a8a7a)}
.photo-homes{left:292px;top:189px;width:252px;height:161px;background:linear-gradient(135deg,#5e7a4a,#8a8a80 50%,#4f6e45)}
.back-mark{left:596px;top:18px;width:150px;height:150px;border-radius:50%;background:var(--red);border:6px solid var(--navy)}
.back-name{left:596px;top:72px;width:150px;text-align:center;font-family:"Archivo Black",sans-serif;font-size:24px;line-height:1.05;color:var(--white)}
.contact-list{left:574px;top:184px;list-style:none}
.contact-list li{display:flex;align-items:flex-start;gap:9px;color:var(--navy);font-weight:500;font-size:15.5px;line-height:1.18;margin-bottom:13px}
.contact-list li.phone{font-weight:700;font-size:18.5px;margin-bottom:13px}
.icon{flex:none;width:18px;height:18px;margin-top:1px}
.follow{left:596px;top:335px;display:flex;align-items:center;gap:14px;font-weight:800;font-style:italic;font-size:13px;color:var(--orange)}
.social{width:25px;height:25px;border-radius:50%;background:var(--navy);display:inline-block}
.social.alt{background:var(--orange);margin-left:-8px}
.divider{left:781px;top:28px;height:330px;border-left:1.5px dashed var(--line)}
.indicia{left:1059px;top:26px;width:93px;height:97px;border:1px solid #777;font-size:10px;color:#333;text-align:center;line-height:1.45;padding-top:10px}
.indicia strong{display:block;font-size:15px;line-height:1.1}
.address-line{left:807px;width:346px;border-top:1px solid #555}
</style>
</head>
<body>
<div class="canvas">

  <section class="front abs">
    <div class="pool-photo abs" role="img" aria-label="Rippling blue pool water with tiled floor"></div>

    <div class="brand-mark abs"></div>
    <div class="brand-name abs">Tide<br>Sweepers</div>

    <h1 class="headline abs">A CLEAN POOL</h1>
    <div class="script abs">Feels Like Vacation!</div>
    <p class="tagline abs">LOCAL. RELIABLE. FAMILY-OWNED.<br>PROUDLY SERVING SAN DIEGO</p>

    <div class="city-badge abs" role="img" aria-label="San Diego city badge with palm trees at sunset"></div>

    <div class="offer abs">
      <span class="offer-get abs">GET</span>
      <span class="offer-amount abs"><sup>$</sup>50</span>
      <p class="offer-copy abs">OFF YOUR<br>FIRST MONTH<br>OF SERVICE</p>
      <div class="offer-pill abs">
        <svg width="22" height="22" viewBox="0 0 22 22"><circle cx="11" cy="11" r="11" fill="var(--orange)"/><path d="M6 11.5l3.5 3.5L16 8" stroke="#fff" stroke-width="2.6" fill="none" stroke-linecap="round"/></svg>
        MENTION THIS CARD WHEN YOU SIGN UP!
      </div>
    </div>

    <div class="trust-bar abs">
      <div class="trust-item trust-family abs">
        <svg width="26" height="28" viewBox="0 0 26 28"><path d="M13 1L2 5v8c0 7 5 12 11 14 6-2 11-7 11-14V5z" fill="var(--navy)" stroke="#fff" stroke-width="1.5"/><path d="M8 14l3.5 3.5L18 10" stroke="#fff" stroke-width="2.6" fill="none"/></svg>
        FAMILY OWNED &amp; OPERATED
      </div>
      <div class="trust-item trust-guarantee abs">
        <svg width="26" height="28" viewBox="0 0 26 28"><path d="M13 1L2 5v8c0 7 5 12 11 14 6-2 11-7 11-14V5z" fill="var(--red)" stroke="#fff" stroke-width="1.5"/><path d="M8 14l3.5 3.5L18 10" stroke="#fff" stroke-width="2.6" fill="none"/></svg>
        100% SATISFACTION GUARANTEED
      </div>
      <div class="trust-item trust-licensed abs">
        <svg width="26" height="28" viewBox="0 0 26 28"><path d="M13 1L2 5v8c0 7 5 12 11 14 6-2 11-7 11-14V5z" fill="var(--red)" stroke="#fff" stroke-width="1.5"/><path d="M8 14l3.5 3.5L18 10" stroke="#fff" stroke-width="2.6" fill="none"/></svg>
        LICENSED &amp; INSURED
      </div>
    </div>

    <div class="contact-tab abs"></div>
    <div class="phone-disc abs">
      <svg width="26" height="26" viewBox="0 0 24 24"><path d="M6.6 10.8a15 15 0 006.6 6.6l2.2-2.2a1 1 0 011-.25 11.4 11.4 0 003.6.57 1 1 0 011 1V20a1 1 0 01-1 1A17 17 0 013 4a1 1 0 011-1h3.5a1 1 0 011 1c0 1.250.2 2.45.57 3.57a1 1 0 01-.25 1z" fill="var(--orange)"/></svg>
    </div>
    <div class="tab-phone abs">619-555-0148</div>
    <div class="tab-site abs">TideSweepers.com</div>
  </section>

  <section class="back abs">
    <h2 class="services-title abs">OUR POOL &amp; SPA</h2>
    <div class="services-script abs">Services</div>
    <div class="services-rule abs"></div>
    <div class="truck-photo abs" role="img" aria-label="Branded company pickup truck"></div>

    <ul class="service-list abs">
      <li><svg width="15" height="16" viewBox="0 0 26 28"><path d="M13 1L2 5v8c0 7 5 12 11 14 6-2 11-7 11-14V5z" fill="var(--red)"/><path d="M8 14l3.5 3.5L18 10" stroke="#fff" stroke-width="3" fill="none"/></svg>WEEKLY POOL CLEANING</li>
      <li><svg width="15" height="16" viewBox="0 0 26 28"><path d="M13 1L2 5v8c0 7 5 12 11 14 6-2 11-7 11-14V5z" fill="var(--red)"/><path d="M8 14l3.5 3.5L18 10" stroke="#fff" stroke-width="3" fill="none"/></svg>WATER BALANCING &amp; CHEMICALS</li>
      <li><svg width="15" height="16" viewBox="0 0 26 28"><path d="M13 1L2 5v8c0 7 5 12 11 14 6-2 11-7 11-14V5z" fill="var(--red)"/><path d="M8 14l3.5 3.5L18 10" stroke="#fff" stroke-width="3" fill="none"/></svg>EQUIPMENT INSPECTIONS</li>
      <li><svg width="15" height="16" viewBox="0 0 26 28"><path d="M13 1L2 5v8c0 7 5 12 11 14 6-2 11-7 11-14V5z" fill="var(--red)"/><path d="M8 14l3.5 3.5L18 10" stroke="#fff" stroke-width="3" fill="none"/></svg>FILTER CLEANING</li>
      <li><svg width="15" height="16" viewBox="0 0 26 28"><path d="M13 1L2 5v8c0 7 5 12 11 14 6-2 11-7 11-14V5z" fill="var(--red)"/><path d="M8 14l3.5 3.5L18 10" stroke="#fff" stroke-width="3" fill="none"/></svg>GREEN POOL RECOVERY</li>
      <li><svg width="15" height="16" viewBox="0 0 26 28"><path d="M13 1L2 5v8c0 7 5 12 11 14 6-2 11-7 11-14V5z" fill="var(--red)"/><path d="M8 14l3.5 3.5L18 10" stroke="#fff" stroke-width="3" fill="none"/></svg>SPA &amp; HOT TUB CARE</li>
      <li><svg width="15" height="16" viewBox="0 0 26 28"><path d="M13 1L2 5v8c0 7 5 12 11 14 6-2 11-7 11-14V5z" fill="var(--red)"/><path d="M8 14l3.5 3.5L18 10" stroke="#fff" stroke-width="3" fill="none"/></svg>RELIABLE &amp; ON-TIME SERVICE</li>
    </ul>

    <div class="photo-pool abs" role="img" aria-label="Aerial view of a backyard pool and spa surrounded by lawn"></div>
    <div class="photo-homes abs" role="img" aria-label="Aerial view of a neighborhood with many backyard pools"></div>

    <div class="back-mark abs"></div>
    <div class="back-name abs">Tide<br>Sweepers</div>

    <ul class="contact-list abs">
      <li class="phone"><svg class="icon" viewBox="0 0 24 24"><circle cx="12" cy="12" r="12" fill="var(--navy)"/><path d="M8.6 10.6a9 9 0 004.8 4.8l1.4-1.4a.7.7 0 01.7-.17 7 7 0 002.2.35.7.7 0 01.7.7v2.2a.7.7 0 01-.7.7A11 11 0 016 6.7a.7.7 0 01.7-.7h2.2a.7.7 0 01.7.7c0 .77.12 1.5.35 2.2a.7.7 0 01-.17.7z" fill="#fff"/></svg>619-555-0148</li>
      <li><svg class="icon" viewBox="0 0 24 24"><circle cx="12" cy="12" r="12" fill="var(--navy)"/><circle cx="12" cy="12" r="6.5" fill="none" stroke="#fff" stroke-width="1.4"/><path d="M5.5 12h13M12 5.5c-2.5 3-2.5 10 0 13M12 5.5c2.5 3 2.5 10 0 13" stroke="#fff" stroke-width="1.2" fill="none"/></svg>TideSweepers.com</li>
      <li><svg class="icon" viewBox="0 0 24 24"><circle cx="12" cy="12" r="12" fill="var(--navy)"/><rect x="6" y="8" width="12" height="8.5" rx="1" fill="none" stroke="#fff" stroke-width="1.4"/><path d="M6 8.5l6 4.5 6-4.5" stroke="#fff" stroke-width="1.4" fill="none"/></svg>hello@tidesweepers.com</li>
      <li><svg class="icon" viewBox="0 0 24 24"><path d="M12 1a8 8 0 00-8 8c0 6 8 14 8 14s8-8 8-14a8 8 0 00-8-8z" fill="var(--navy)"/><circle cx="12" cy="9" r="3" fill="#fff"/></svg>4820 Harbor Crest Ave.<br>San Diego, CA 92107</li>
    </ul>

    <div class="follow abs">FOLLOW US! <span class="social"></span><span class="social alt"></span></div>

    <div class="divider abs"></div>

    <div class="indicia abs">PRSRT STD<br>ECRWSS<br>U.S. POSTAGE<strong>PAID</strong>EDDM RETAIL</div>

    <div class="address-line abs" style="top:204px"></div>
    <div class="address-line abs" style="top:241px"></div>
    <div class="address-line abs" style="top:279px"></div>
    <div class="address-line abs" style="top:316px"></div>
  </section>

</div>
</body>
</html>
```